Business Card Design

Supporting people with a spinal cord injury

Industry/Entity Type

Business

Contact Information for Business Card

FRONT
Marcy Quellton
Service Coordinator
57 Fenwick Lane, West Mackay QLD 4740
Tel: (07) 4063 8815
Fax: (07) 4063 8819
after hours: 0498761137
marcy@trovex.org.au
www.trovex.org.au

BACK - little text to fit
* Personal care and lifestyle assistance
* Supported accommodation - temporary, respite and transition (Kolo-haven)
* Transition Support Program for residents of Kolo-haven with a SCI
* In-home respite support
* Community Access
* In-home support for people in the community
* Wheelchair accessible transport
* Equipment loan
* Use of Brisk core Gym to work on upper body strength
* SCI awareness and prevention
* Information and community linking
* Assist people with obtaining equipment
* 3 accessible, 2bedroom rental units in Andergrove
* After hours emergency support service
BEINF INSPIRED AND INSPIRING OTHERS

```html
<!DOCTYPE html>
<html lang="en">
<head>
<meta charset="utf-8">
<title>Trovex Business Card</title>
<link href="https://fonts.googleapis.com/css2?family=Exo+2:wght@400;500;700&display=swap" rel="stylesheet">
<style>
  :root {
    --backdrop: #e9e6df;
    --card: #ffffff;
    --ink: #1d1d1b;
    --muted: #6b6b6b;
    --green: #8cc63f;
    --orange: #f7a11a;
    --white: #ffffff;
  }
  * { margin: 0; padding: 0; box-sizing: border-box; }
  html, body {
    width: 1200px; height: 899px; overflow: hidden;
    background: var(--backdrop);
    font-family: "Exo 2", sans-serif;
  }
  .card {
    position: absolute; left: 100px; top: 164px;
    width: 1000px; height: 571px;
    background: var(--card);
    box-shadow: 0 14px 40px rgba(0,0,0,0.18);
    overflow: hidden;
  }
  .card-sweep { position: absolute; inset: 0; width: 1000px; height: 571px; }
  .brand {
    position: absolute; left: 70px; top: 90px;
    display: flex; align-items: center; gap: 22px;
  }
  .brand-dot {
    width: 70px; height: 70px; border-radius: 50%;
    background: var(--green);
  }
  .brand-name {
    font-size: 92px; font-weight: 700; color: var(--ink);
    letter-spacing: 2px; line-height: 0.9;
  }
  .brand-tagline {
    font-size: 13px; font-weight: 400; color: var(--muted);
    margin-top: 6px; letter-spacing: 0.3px;
  }
  .address {
    position: absolute; left: 80px; top: 296px;
    font-size: 25px; font-weight: 500; color: var(--ink);
    line-height: 1.35; letter-spacing: 1px;
  }
  .contacts {
    position: absolute; left: 80px; top: 390px;
    list-style: none;
    font-size: 21px; color: var(--ink); letter-spacing: 1px;
  }
  .contacts li { display: flex; align-items: center; gap: 14px; height: 34px; }
  .contacts svg { width: 20px; height: 20px; fill: var(--ink); flex: none; }
  .holder {
    position: absolute; right: 40px; top: 384px;
    text-align: right; color: var(--white); letter-spacing: 2px;
  }
  .holder-name { font-size: 26px; font-weight: 500; }
  .holder-role { font-size: 19px; font-weight: 400; margin-top: 4px; }
</style>
</head>
<body>
  <div class="card">
    <svg class="card-sweep" viewBox="0 0 1000 571" aria-hidden="true">
      <path d="M680 0 Q560 290 760 571 L1000 571 L1000 0 Z" fill="var(--orange)"/>
      <path d="M690 0 Q570 290 770 571 L1000 571 L1000 0 Z" fill="var(--green)"/>
    </svg>

    <div class="brand">
      <span class="brand-dot"></span>
      <div>
        <div class="brand-name">TROVEX</div>
        <div class="brand-tagline">Trovex Regional Spinal Support Network Inc</div>
      </div>
    </div>

    <p class="address">57 Fenwick Lane,<br>West Mackay QLD 4740</p>

    <ul class="contacts">
      <li>
        <svg viewBox="0 0 24 24"><path d="M6.6 10.8a15.1 15.1 0 0 0 6.6 6.6l2.2-2.2a1 1 0 0 1 1-.25 11.4 11.4 0 0 0 3.6.57 1 1 0 0 1 1 1V20a1 1 0 0 1-1 1A17 17 0 0 1 3 4a1 1 0 0 1 1-1h3.5a1 1 0 0 1 1 1c0 1.25.2 2.45.57 3.57a1 1 0 0 1-.25 1z"/></svg>
        (07) 4063 8815
      </li>
      <li>
        <svg viewBox="0 0 24 24"><path d="M7 2h8l4 4v4H7zm-3 9h16a2 2 0 0 1 2 2v8H2v-8a2 2 0 0 1 2-2zm3 3v2h2v-2zm4 0v2h2v-2zm4 0v2h2v-2zm-8 4v2h2v-2zm4 0v2h2v-2z"/></svg>
        (07) 4063 8819
      </li>
      <li>
        <svg viewBox="0 0 24 24"><path d="M7 1h10a2 2 0 0 1 2 2v18a2 2 0 0 1-2 2H7a2 2 0 0 1-2-2V3a2 2 0 0 1 2-2zm0 3v14h10V4zm5 15.5a1.2 1.2 0 1 0 0 2.4 1.2 1.2 0 0 0 0-2.4z"/></svg>
        0498761137
      </li>
      <li>
        <svg viewBox="0 0 24 24"><path d="M2 5h20v14H2zm2 2v.5l8 5.5 8-5.5V7z"/></svg>
        marcy@trovex.org.au
      </li>
      <li>
        <svg viewBox="0 0 24 24"><path d="M12 2a10 10 0 1 0 0 20 10 10 0 0 0 0-20zm6.9 6h-2.9a15 15 0 0 0-1.4-3.9A8 8 0 0 1 18.9 8zM12 4c.8 1.1 1.5 2.5 1.9 4h-3.8c.4-1.5 1.1-2.9 1.9-4zM4.3 14a8 8 0 0 1 0-4h3.3a16 16 0 0 0 0 4zm.8 2h2.9a15 15 0 0 0 1.4 3.9A8 8 0 0 1 5.1 16zM8 8H5.1a8 8 0 0 1 4.3-3.9A15 15 0 0 0 8 8zm4 12c-.8-1.1-1.5-2.5-1.9-4h3.8c-.4 1.5-1.1 2.9-1.9 4zm2.3-6H9.7a14 14 0 0 1 0-4h4.6a14 14 0 0 1 0 4zm.3 5.9a15 15 0 0 0 1.4-3.9h2.9a8 8 0 0 1-4.3 3.9zM16.4 14a16 16 0 0 0 0-4h3.3a8 8 0 0 1 0 4z"/></svg>
        www.trovex.org.au
      </li>
    </ul>

    <div class="holder">
      <div class="holder-name">MARCY QUELLTON</div>
      <div class="holder-role">SERVICE COORDINATOR</div>
    </div>
  </div>
</body>
</html>
```